50% off blue price stickers - poster

I am looking for a poster to hang in our retail discount store that let's people know they take 50% off the marked price on anything with a blue price sticker. We try and tell them as they walk in but can't catch everyone. If they don't know, they don't see the value in the pricing. We mark the retail price with a blue price tag and they get 50% off that price. We sell items from wholesale clubs (Valmo, JEDs Depot) and offer 50% off what they sell the items for. Clothes, Housewares, Kitchenware, Furniture, Bath and Body, Electronics, Jewelry - you name it.
Updates

Check out our Linkpage page - Marla's Double Delight, in Brentwood, California to learn more about us and our merchandise.

For poster size - we are looking at 20" wide by 30" long. Thank you.

Target Market(s)

Ages 35-50

Industry/Entity Type

Retail

Font styles to use
Serif

Requirements
Must have
• Store name - Marla's Double Delight
Nice to have
• Not too cluttered - easy to read to get the point across quickly. Something that incorporates our logo - but doesn't have to stick with the red/black theme, especially if you are using blue themes in the poster. Maybe just use the theme of the logo so the fonts are similar....

```html
<!DOCTYPE html>
<html lang="en">
<head>
<meta charset="utf-8">
<title>Double Delight – 50% Off Blue Price Tag Poster</title>
<link rel="stylesheet" href="https://fonts.googleapis.com/css2?family=Anton&family=Open+Sans:wght@700;800&family=Patrick+Hand&display=swap">
<style>
  :root {
    --backdrop: #e9e9ea;
    --paper: #ffffff;
    --sale-red: #e61f26;
    --sale-orange: #f26522;
    --ink: #333333;
    --tag-blue: #29abe2;
    --brand-red: #d71f27;
  }
  html, body {
    margin: 0;
    padding: 0;
    width: 879px;
    height: 1200px;
    overflow: hidden;
    background: var(--backdrop);
  }
  .canvas {
    width: 879px;
    height: 1200px;
    display: flex;
    justify-content: center;
    align-items: center;
  }
  .poster {
    display: block;
    width: 798px;
    height: 1200px;
  }
  .script-line {
    font-family: "Patrick Hand", cursive;
    fill: var(--paper);
  }
  .headline-figure {
    font-family: "Anton", sans-serif;
    fill: var(--paper);
    stroke: var(--ink);
    stroke-width: 10;
    paint-order: stroke fill;
    stroke-linejoin: round;
  }
  .tag-word {
    font-family: "Open Sans", sans-serif;
    font-weight: 800;
    fill: var(--paper);
  }
  .store-name {
    font-family: "Open Sans", sans-serif;
    font-weight: 700;
    fill: var(--brand-red);
  }
</style>
</head>
<body>
<main class="canvas">
  <svg class="poster" viewBox="0 0 750 1128" xmlns="http://www.w3.org/2000/svg" aria-label="Take 50% off of any blue price tag – Double Delight">
    <defs>
      <linearGradient id="burst" x1="0" y1="0" x2="1" y2="1">
        <stop offset="0" stop-color="var(--sale-red)"/>
        <stop offset="0.55" stop-color="#ef4423"/>
        <stop offset="1" stop-color="var(--sale-orange)"/>
      </linearGradient>
    </defs>

    <rect class="poster-paper" width="750" height="1128" fill="var(--paper)"/>

    <path class="sale-burst" role="img" aria-label="Red to orange halftone burst background"
          fill="url(#burst)"
          d="M0 0 H750 V840 C700 860 650 875 600 885 L508 1003 L500 900 C330 880 160 840 0 790 Z"/>

    <text class="script-line" x="130" y="140" font-size="74" transform="rotate(-4 220 120)">Take</text>

    <g class="headline" transform="rotate(-3 280 380)">
      <text class="headline-figure" x="8" y="570" font-size="470" textLength="535" lengthAdjust="spacingAndGlyphs">50</text>
      <text class="headline-figure" x="560" y="350" font-size="250" textLength="160" lengthAdjust="spacingAndGlyphs">%</text>
      <text class="headline-figure" x="558" y="480" font-size="122" textLength="190" lengthAdjust="spacingAndGlyphs">OFF</text>
    </g>

    <text class="script-line" x="215" y="648" font-size="78" transform="rotate(-8 340 620)">of any</text>

    <path class="tag-string" d="M555 766 C520 700 560 560 640 455" fill="none" stroke="var(--ink)" stroke-width="2.5"/>

    <g class="blue-tag">
      <path d="M163 723 L518 655 L593 753 L568 853 L200 950 Z" fill="var(--tag-blue)"/>
      <circle cx="555" cy="766" r="11" fill="var(--sale-orange)" stroke="var(--ink)" stroke-width="3"/>
      <g transform="rotate(-12 360 800)">
        <text class="tag-word" x="220" y="820" font-size="96" textLength="300" lengthAdjust="spacingAndGlyphs">BLUE</text>
        <text class="tag-word" x="222" y="880" font-size="50" font-weight="700" textLength="290" lengthAdjust="spacingAndGlyphs">PRICE TAG</text>
      </g>
    </g>

    <text class="store-name" x="375" y="1090" font-size="78" text-anchor="middle" textLength="570" lengthAdjust="spacingAndGlyphs">Double Delight</text>
  </svg>
</main>
</body>
</html>
```